Design a Bold Banner for Fitness Club

We need a Bold, Eye Catching Banner created in order to capture the attention of potential new members.
The banner size will be horizontal 4'w x 6' L
Our colors are typically Black - White - Yellow, but we're looking for something that pops from a distance, so these colors can be changed.
I'd like the font's to be bold - easy to read - eye catching - with some design elements
I have attached our logo to this message as well as a pdf with the text and layout.
I would like to use as much space on the banner as possible (not having all text centered / small with a bunch of blank space around) while still having the banner look GREAT!
Thank you and I look forward to seeing your design.
UPDATE: I have reviewed the submissions this far and they are all very busy. We need a banner that is VERY easy to read upon driving by, but with some slight design elements.
I have now uploaded some example photos that quillmerton.com has on their site as an example of how I'd like people to easy see, read and take action with.

```html
<!DOCTYPE html>
<html lang="en">
<head>
<meta charset="utf-8">
<title>Pulsefit – Tired of Being Fat &amp; Ugly</title>
<link rel="stylesheet" href="https://fonts.googleapis.com/css2?family=Abril+Fatface&family=Archivo+Black&family=Titan+One&family=Playfair+Display:wght@900&display=swap">
<style>
  :root {
    --wall-light: #6f8088;
    --wall-mid: #4d5d6b;
    --wall-dark: #2c3848;
    --ink-white: #f4f4f4;
    --ink-red: #e3000f;
    --ink-black: #0a0a0a;
    --photo-top: #b89a62;
    --photo-mid: #9c7c55;
    --photo-bottom: #6e5a45;
  }
  * { margin: 0; padding: 0; box-sizing: border-box; }
  html, body { width: 1200px; height: 533px; overflow: hidden; background: var(--wall-mid); }
  .banner { display: block; width: 1200px; height: 533px; }
  .headline-kicker {
    font-family: "Abril Fatface", serif;
    fill: var(--ink-white);
    stroke: var(--ink-black);
    stroke-width: 1.5;
    paint-order: stroke;
  }
  .headline-kicker-shadow { font-family: "Abril Fatface", serif; fill: var(--ink-red); }
  .headline-main {
    font-family: "Archivo Black", sans-serif;
    fill: var(--ink-white);
    stroke: var(--ink-red);
    stroke-width: 5;
    paint-order: stroke;
  }
  .headline-amp {
    font-family: "Playfair Display", serif;
    font-weight: 900;
    fill: var(--ink-white);
    stroke: var(--ink-red);
    stroke-width: 5;
    paint-order: stroke;
  }
  .headline-answer {
    font-family: "Titan One", sans-serif;
    fill: var(--ink-white);
    stroke: var(--ink-red);
    stroke-width: 5;
    paint-order: stroke;
  }
  .shadow-text { fill: var(--ink-black); stroke: none; }
  .club-name { font-family: "Titan One", sans-serif; fill: var(--ink-black); }
</style>
</head>
<body>
<svg class="banner" viewBox="0 0 1200 533" xmlns="http://www.w3.org/2000/svg">
  <defs>
    <radialGradient id="wall" cx="0.45" cy="0.5" r="0.75">
      <stop offset="0" stop-color="var(--wall-light)"/>
      <stop offset="0.6" stop-color="var(--wall-mid)"/>
      <stop offset="1" stop-color="var(--wall-dark)"/>
    </radialGradient>
    <linearGradient id="photo-fill" x1="0" y1="0" x2="0" y2="1">
      <stop offset="0" stop-color="var(--photo-top)"/>
      <stop offset="0.5" stop-color="var(--photo-mid)"/>
      <stop offset="1" stop-color="var(--photo-bottom)"/>
    </linearGradient>
    <filter id="soft" x="-10%" y="-10%" width="120%" height="120%">
      <feGaussianBlur stdDeviation="4"/>
    </filter>
  </defs>

  <rect class="wall" width="1200" height="533" fill="url(#wall)"/>

  <rect class="hero-photo" x="913" y="84" width="205" height="449" fill="url(#photo-fill)"
        role="img" aria-label="Photo of a muscular shirtless man with a paper bag over his head"/>

  <text class="headline-kicker-shadow" x="80" y="75" font-size="84" textLength="685" lengthAdjust="spacingAndGlyphs">TIRED OF BEING</text>
  <text class="headline-kicker" x="77" y="68" font-size="84" textLength="685" lengthAdjust="spacingAndGlyphs">TIRED OF BEING</text>

  <g class="text-shadow" filter="url(#soft)" opacity="0.75">
    <text class="shadow-text" x="20" y="248" font-size="175" textLength="309" lengthAdjust="spacingAndGlyphs" font-family="Archivo Black, sans-serif">FAT</text>
    <text class="shadow-text" x="512" y="240" font-size="170" textLength="391" lengthAdjust="spacingAndGlyphs" font-family="Archivo Black, sans-serif">UGLY</text>
    <text class="shadow-text" x="22" y="374" font-size="140" textLength="796" lengthAdjust="spacingAndGlyphs" font-family="Titan One, sans-serif">just be ugly</text>
  </g>

  <text class="headline-main" x="33" y="232" font-size="175" textLength="309" lengthAdjust="spacingAndGlyphs">FAT</text>
  <text class="headline-amp" x="373" y="236" font-size="180" textLength="112" lengthAdjust="spacingAndGlyphs">&amp;</text>
  <text class="headline-main" x="524" y="226" font-size="170" textLength="391" lengthAdjust="spacingAndGlyphs">UGLY</text>

  <text class="headline-answer" x="33" y="356" font-size="140" textLength="796" lengthAdjust="spacingAndGlyphs">just be ugly</text>

  <text class="club-name" x="182" y="494" font-size="115" textLength="465" lengthAdjust="spacingAndGlyphs">Pulsefit</text>
</svg>
</body>
</html>
```